The name of my company is Tolland Refacing LLC and I would like the sub text to say "Cabinet Refacing and Countertops". Have my name Morris Pelton, Owner / Sales, contact info: Cell: 360-555-0147 / Email: morris.pelton@quillbox.net

Simple, Clean, and Organized. With colors that will appeal to the eye.

Target Market(s)

Houses and Apartments

Industry/Entity Type

Cabinet Refacing

Contact Information for Business Card

Company name and sub text Morris Pelton - Owner / Sales, my cell phone number and email

Requirements
Must have
• Business name, my name / position, and my contact info
Nice to have
• Simple. Organized. Appealing to the eye

```html
<!DOCTYPE html>
<html lang="en">
<head>
<meta charset="UTF-8">
<title>Tolland Refacing LLC – Business Card</title>
<link href="https://fonts.googleapis.com/css2?family=Quicksand:wght@300;500&family=Roboto:wght@300;400;700&display=swap" rel="stylesheet">
<style>
  :root {
    --stage: #3b3e43;
    --card-white: #ffffff;
    --brand-blue: #4070bb;
    --name-grey: #8b9bb3;
    --ink: #2a2a2a;
    --paper-text: #ffffff;
  }
  html, body {
    margin: 0;
    padding: 0;
    width: 1200px;
    height: 800px;
    overflow: hidden;
    background: var(--stage);
  }
  .canvas {
    position: relative;
    width: 1200px;
    height: 800px;
  }
  .card {
    position: absolute;
    top: 256px;
    width: 480px;
    height: 288px;
    box-shadow: 0 4px 10px rgba(0,0,0,0.35);
    overflow: hidden;
  }
  .card--front {
    left: 89px;
    background: var(--card-white);
  }
  .card--back {
    left: 632px;
    background: var(--brand-blue);
  }
  .brand-mark {
    position: absolute;
    left: 50%;
    top: 88px;
    width: 42px;
    height: 42px;
    margin-left: -21px;
    border-radius: 50%;
    background: var(--brand-blue);
  }
  .brand-name {
    position: absolute;
    left: 0;
    right: 0;
    top: 146px;
    margin: 0;
    text-align: center;
    font-family: "Quicksand", sans-serif;
    font-weight: 300;
    font-size: 24px;
    line-height: 28px;
    letter-spacing: 0.3px;
    color: var(--name-grey);
    text-transform: uppercase;
    white-space: nowrap;
  }
  .brand-tagline {
    position: absolute;
    left: 0;
    right: 0;
    top: 182px;
    margin: 0;
    text-align: center;
    font-family: "Quicksand", sans-serif;
    font-weight: 500;
    font-size: 13.5px;
    line-height: 16px;
    color: var(--ink);
  }
  .service-band {
    position: absolute;
    left: 0;
    right: 0;
    top: 218px;
    height: 34px;
    background: var(--brand-blue);
    color: var(--paper-text);
    font-family: "Roboto", sans-serif;
    font-weight: 300;
    font-size: 20px;
    line-height: 34px;
    text-align: center;
    letter-spacing: -0.3px;
    white-space: nowrap;
  }
  .back-lockup {
    position: absolute;
    left: 0;
    right: 0;
    top: 118px;
    text-align: center;
    color: var(--paper-text);
  }
  .back-lockup-inner {
    display: inline-block;
  }
  .back-name {
    margin: 0;
    font-family: "Roboto", sans-serif;
    font-weight: 700;
    font-size: 25px;
    line-height: 30px;
    letter-spacing: -0.5px;
    white-space: nowrap;
  }
  .back-sub {
    margin: 3px 0 0;
    border-top: 1px solid var(--paper-text);
    border-bottom: 1px solid var(--paper-text);
    font-family: "Roboto", sans-serif;
    font-weight: 300;
    font-size: 10.5px;
    line-height: 13px;
    letter-spacing: -0.2px;
    white-space: nowrap;
  }
  .contact {
    position: absolute;
    left: 0;
    right: 0;
    top: 196px;
    margin: 0;
    text-align: center;
    font-style: normal;
    font-family: "Roboto", sans-serif;
    color: var(--paper-text);
  }
  .contact-person {
    margin: 0;
    font-weight: 400;
    font-size: 12px;
    line-height: 16px;
  }
  .contact-role {
    font-weight: 300;
  }
  .contact-line {
    margin: 2px 0 0;
    font-weight: 300;
    font-size: 10.5px;
    line-height: 14px;
    white-space: nowrap;
  }
</style>
</head>
<body>
  <main class="canvas">
    <section class="card card--front">
      <span class="brand-mark" aria-hidden="true"></span>
      <h1 class="brand-name">Tolland Refacing, LLC</h1>
      <p class="brand-tagline">Cabinets and Countertops</p>
      <div class="service-band">CABINET REFACING AND COUNTERTOPS</div>
    </section>
    <section class="card card--back">
      <div class="back-lockup">
        <div class="back-lockup-inner">
          <h2 class="back-name">TOLLAND REFACING LLC</h2>
          <p class="back-sub">CABINET REFACING AND COUNTERTOPS</p>
        </div>
      </div>
      <address class="contact">
        <p class="contact-person">Morris Pelton <span class="contact-role">– Owner / Sales</span></p>
        <p class="contact-line">Cell: 360-555-0147 &nbsp;/&nbsp; Email: morris.pelton@quillbox.net</p>
      </address>
    </section>
  </main>
</body>
</html>
```